Dorian's Lawn Service needs a postcard design

I need a design to attract lawn cutting customers. I am a high school junior, focusing on my city and the neighboring city. I think it would be advantageous to let my potential clients know I am earning money for my college education. They should also know, I will be working side by side with my father, who operated his own lawn service for 20 years, so they can be assured of a quality result for their lawn. I will be using state of the art, commercial equipment.

A few things that are unique to my service are; my mower weighs half of what other commercial mowers do (a softer footprint), my mower does NOT throw clippings into mulch or flower beds, at an additional charge I offer bagging of the clippings and/or dog waste clean-up. I am thinking about a two-sided design. I would also like a cartoon style picture of myself riding my mower. If this is something you can create, I can send you a photo of myself and a photo of my mower. If not, I can get this drawing done separately, then send it to you, I would just need to know what kind of file you would need it in. I am not going to have a business name, I want to introduce myself as Dorian to keep it simple and personal. We can add a coupon to the postcard, offering one free cut with commitment to a full 26 week season. The name of my high school is Marlowe High.

The cartoon picture attached is our logo.

Target Market(s)

Homeowners that use a commercial lawn cutting service, homeowners that need a temporary service while they are on vacation

Industry/Entity Type

School

Colors
3176b5
9bcb3c

Requirements
Must have
• An appeal for people to want to help me earn money for my college education. A clear idea they will be getting top notch service. I definitely want a drawing of myself on my mower. Phone # 612-905-3817
• design must work with parcelvaro.com/routeflyermailing guidelines

```html
<!DOCTYPE html>
<html lang="en">
<head>
<meta charset="utf-8">
<title>Dorian's Lawn Service – Postcard</title>
<link rel="stylesheet" href="https://fonts.googleapis.com/css2?family=Exo+2:ital,wght@1,800&family=Play:wght@400;700&display=swap">
<style>
  :root {
    --lime: #9bcb3c;
    --lime-light: #b5d95e;
    --blue: #3176b5;
    --blue-deep: #1d6aa8;
    --navy: #1e2633;
    --ink: #1a1a1a;
    --white: #ffffff;
    --paper: #f7f8f6;
  }
  * { margin: 0; padding: 0; box-sizing: border-box; }
  html, body { width: 1200px; height: 849px; overflow: hidden; background: var(--white); }
  .postcard {
    position: relative;
    width: 1200px;
    height: 849px;
    background: var(--paper);
    font-family: "Play", sans-serif;
    color: var(--ink);
    overflow: hidden;
  }
  .backdrop { position: absolute; inset: 0; }
  .brand-title {
    position: absolute;
    top: 18px; left: 0; width: 1200px;
    text-align: center;
    font-family: "Exo 2", sans-serif;
    font-style: italic;
    font-weight: 800;
    font-size: 82px;
    letter-spacing: 1px;
    color: var(--blue-deep);
    -webkit-text-stroke: 3px var(--white);
    paint-order: stroke fill;
    padding-left: 40px;
  }
  .greeting { position: absolute; left: 0; top: 0; width: 600px; height: 849px; }
  .call-now {
    position: absolute;
    left: 30px; top: 732px;
    font-weight: 700;
    font-size: 38px;
    color: var(--navy);
    display: flex; align-items: center; gap: 14px;
  }
  .call-now .dots { width: 250px; height: 6px;
    background: radial-gradient(circle, var(--blue) 2.6px, transparent 3px) 0 0 / 16px 6px repeat-x; }
  .phone {
    position: absolute;
    left: 150px; top: 772px;
    font-weight: 700;
    font-size: 42px;
    color: var(--blue);
    letter-spacing: 1px;
  }
  .phone::before { content: "• •"; margin-right: 26px; font-size: 30px; vertical-align: middle; }

  .why-panel {
    position: absolute;
    left: 566px; top: 156px;
    width: 592px; height: 668px;
    border: 9px solid var(--lime);
    border-radius: 34px;
    background: var(--white);
    text-align: center;
    padding-top: 12px;
  }
  .intro { font-size: 19px; line-height: 27px; color: var(--ink); }
  .why-heading {
    font-weight: 700;
    font-size: 42px;
    line-height: 50px;
    color: var(--blue-deep);
    margin: 0 0 10px;
  }
  .section-band {
    background: var(--blue-deep);
    color: var(--white);
    font-size: 24px;
    font-weight: 400;
    line-height: 38px;
    height: 38px;
    margin: 0 6px;
  }
  .advantages { list-style: none; }
  .advantages li {
    font-size: 19px;
    font-weight: 700;
    line-height: 27px;
    height: 72px;
    padding: 4px 12px 0;
    position: relative;
  }
  .advantages li::after {
    content: "";
    position: absolute;
    left: 50%; bottom: 6px;
    width: 90px; height: 6px;
    transform: translateX(-50%);
    background: radial-gradient(circle, var(--dot, var(--blue)) 2.6px, transparent 3px) 0 0 / 18px 6px repeat-x;
  }
  .advantages li:nth-child(even) { --dot: var(--lime); }
  .advantages.for-you { margin-bottom: 8px; }
  .advantages.for-me li { font-weight: 400; height: 44px; padding-top: 6px; --dot: var(--lime); }
</style>
</head>
<body>
<main class="postcard">
  <svg class="backdrop" width="1200" height="849" viewBox="0 0 1200 849" aria-hidden="true">
    <path d="M0 0 H1200 V150 C1000 165 820 168 640 170 C420 174 210 186 0 200 Z" fill="var(--lime)"/>
    <path d="M0 200 C210 186 420 174 640 170 C820 168 1000 165 1200 150 V160 C1000 178 820 182 640 184 C420 188 210 196 0 214 Z" fill="var(--lime-light)"/>
    <path d="M0 640 C80 760 260 790 380 720 C470 670 560 640 700 660" fill="none" stroke="var(--blue)" stroke-width="26"/>
    <path d="M300 650 C420 600 520 560 640 600" fill="none" stroke="var(--lime)" stroke-width="22"/>
    <path d="M1150 540 C1180 510 1200 505 1200 505 V560 C1185 560 1165 570 1150 580 Z" fill="var(--blue)"/>
    <path d="M1100 800 C1140 780 1180 772 1200 770 V849 H1060 Z" fill="var(--blue)"/>
    <path d="M0 700 C60 760 120 800 0 849 Z" fill="var(--blue)"/>
    <rect x="0" y="732" width="560" height="96" fill="var(--white)"/>
    <path d="M0 828 H560 C600 828 640 849 660 849 H0 Z" fill="var(--lime)"/>
  </svg>

  <h1 class="brand-title">Dorian’s Lawn Service</h1>

  <svg class="greeting" width="600" height="849" viewBox="0 0 600 849">
    <defs>
      <path id="greeting-arc" d="M34 300 A270 270 0 0 1 540 470"/>
    </defs>
    <text font-family="Play, sans-serif" font-weight="700" font-size="46" fill="var(--navy)">
      <textPath href="#greeting-arc" textLength="612" lengthAdjust="spacing">HI! MY NAME IS DORIAN</textPath>
    </text>
    <circle cx="256" cy="470" r="222" fill="var(--blue)" role="img" aria-label="Cartoon illustration of Dorian in a school T-shirt riding his red zero-turn mower"/>
  </svg>

  <div class="call-now">CALL NOW <span class="dots"></span></div>
  <div class="phone">612-905-3817</div>

  <section class="why-panel">
    <p class="intro">I’m a high school junior at Marlowe High &amp; in<br>my spare time I offer top notch lawn service.</p>
    <h2 class="why-heading">WHY ME?</h2>
    <h3 class="section-band">ADVANTAGES FOR YOU</h3>
    <ul class="advantages for-you">
      <li>My mower weighs half of what other commercial<br>mowers do (a softer footprint)</li>
      <li>My mower does NOT throw clippings into mulch<br>or flower beds</li>
      <li>At an additional charge I offer bagging of the<br>clippings and/or dog waste clean-up</li>
      <li>Everything is taken care of while you are on<br>your vacation</li>
      <li>I will be working side by side with my father,<br>who operated his own lawn service for 20 years</li>
    </ul>
    <h3 class="section-band">ADVANTAGES FOR ME</h3>
    <ul class="advantages for-me">
      <li>Earn money for my college education</li>
    </ul>
  </section>
</main>
</body>
</html>
```